Award-winnning Estate Agent needs a premium version of their 'For Sale' board design

We need a premium option for our 'For Sale' board design. We have a standard board that is attached to this brief, but were are looking to have a premium design version that we will use when selling exclusive properties. Our company name is Harbour Lane Estates and the name for this is exclusive selection is: 'The Harbour Collection'. The design needs to work with our current brand, but have a distinctive PREMIUM feel to it. I have uploaded the barnd guidelines and also some of the exisisting logo variations. We do NOT need a new logo but feel free to play around with colours, fonts, sizes etc. for the sign.

Target Market(s)

Property buyers & house hunters

Industry/Entity Type

Real Estate - Residential Property

Font styles to use
Sans Serif

Requirements
Must have
• A premium fee, must be square design, must be easy to read when driving past the sign
Nice to have
• I'm open ot ideas

```html
<!DOCTYPE html>
<html lang="en">
<head>
<meta charset="utf-8">
<title>Harbour Lane Estates – The Harbour Collection For Sale Board</title>
<link rel="stylesheet" href="https://fonts.googleapis.com/css2?family=Montserrat:wght@600;700;800&family=Oswald:wght@600&display=swap">
<style>
  :root {
    --navy: #2e3586;
    --navy-deep: #1c2160;
    --brand-blue: #1177bd;
    --gold: #c9a55c;
    --white: #ffffff;
  }
  html, body {
    margin: 0;
    padding: 0;
    width: 1200px;
    height: 960px;
    overflow: hidden;
    background: var(--white);
  }
  .board {
    display: block;
    width: 1200px;
    height: 960px;
  }
  .frame { fill: var(--navy-deep); }
  .frame-keyline { fill: none; stroke: var(--gold); stroke-width: 2; }
  .panel-white { fill: var(--white); }
  .panel-navy { fill: var(--navy); }
  .panel-gold { fill: var(--gold); }
  .panel-blue { fill: var(--brand-blue); }
  .rule-gold { stroke: var(--gold); stroke-width: 3; }
  .brand-square { fill: var(--brand-blue); }
  .brand-name {
    font-family: "Montserrat", sans-serif;
    font-weight: 700;
    font-size: 44px;
    fill: var(--navy);
  }
  .collection {
    font-family: "Montserrat", sans-serif;
    font-weight: 700;
    font-size: 30px;
    fill: var(--navy-deep);
  }
  .headline {
    font-family: "Montserrat", sans-serif;
    font-weight: 800;
    fill: var(--white);
  }
  .headline-for { font-size: 110px; }
  .headline-sale { font-size: 240px; }
  .phone {
    font-family: "Montserrat", sans-serif;
    font-weight: 800;
    font-size: 106px;
    fill: var(--navy);
  }
  .web {
    font-family: "Oswald", sans-serif;
    font-weight: 600;
    font-size: 50px;
    fill: var(--white);
  }
</style>
</head>
<body>
<svg class="board" viewBox="0 0 1200 960" xmlns="http://www.w3.org/2000/svg" role="img" aria-label="The Harbour Collection by Harbour Lane Estates – For Sale board">
  <!-- outer frame with gold keyline -->
  <rect class="frame" x="200" y="80" width="800" height="800"/>
  <rect class="frame-keyline" x="213" y="93" width="774" height="774"/>

  <!-- brand header -->
  <rect class="panel-white" x="226" y="106" width="748" height="144"/>
  <rect class="brand-square" x="334" y="162" width="36" height="36"/>
  <text class="brand-name" x="388" y="196" textLength="480" lengthAdjust="spacingAndGlyphs">Harbour Lane Estates</text>

  <!-- collection strip -->
  <rect class="panel-gold" x="226" y="250" width="748" height="60"/>
  <text class="collection" x="600" y="291" text-anchor="middle" textLength="580" lengthAdjust="spacing">THE HARBOUR COLLECTION</text>

  <!-- headline band -->
  <rect class="panel-navy" x="226" y="310" width="748" height="360"/>
  <line class="rule-gold" x1="300" y1="447" x2="900" y2="447"/>
  <text class="headline headline-for" x="600" y="424" text-anchor="middle" textLength="250" lengthAdjust="spacingAndGlyphs">FOR</text>
  <text class="headline headline-sale" x="600" y="644" text-anchor="middle" textLength="660" lengthAdjust="spacingAndGlyphs">SALE</text>

  <!-- phone band -->
  <rect class="panel-white" x="226" y="670" width="748" height="104"/>
  <text class="phone" x="600" y="760" text-anchor="middle" textLength="700" lengthAdjust="spacingAndGlyphs">01632 960412</text>

  <!-- web band -->
  <rect class="panel-blue" x="226" y="774" width="748" height="80"/>
  <text class="web" x="600" y="832" text-anchor="middle" textLength="690" lengthAdjust="spacingAndGlyphs">www.harbourlaneestates.co.uk</text>
</svg>
</body>
</html>
```